We need a MODERN credit application banner

We have a program that helps people get pre-qualified for an auto loan. Our current Application page/Success page is dated and does not have the colors we want. I want to use fonts and colors that match our partner CrestLedger (www.crestledger-demo.com). I want to include their powered by logo, tallymark rating logo, and swift4lending logo all in a matching CrestLedger Color scheme. I also need a Favicon that matches your design for the page. I attached our deck so you can get more content. To be clear the application page and success pages below are the targets of this redesign! You can visit www.pbelvoiradvertising-demo.com to get more information from our website or www.swift4lending-demo.com.

Target Market(s)

Car dealers and their consumers

Industry/Entity Type

Automotive

Requirements
Must have
• It must offer the same data that is on the existing art
Nice to have
• Looking for a Clean but Interesting design.
Should not have
• No red and black. Do not change the form fills.

```html
<!DOCTYPE html>
<html lang="en">
<head>
<meta charset="utf-8">
<title>S4L Application and Success Pages</title>
<link href="https://fonts.googleapis.com/css2?family=Figtree:ital,wght@0,400;0,500;0,600;0,700;0,800;1,400;1,500&display=swap" rel="stylesheet">
<style>
:root{
  --bg:#d8dfe8;
  --blue:#02a5cb;
  --blue-dark:#0196b9;
  --blue-soft:#e3f4fa;
  --yellow:#fde13b;
  --yellow-deep:#f6c800;
  --ink:#2f3a40;
  --muted:#6f7c85;
  --line:#c9d3da;
  --bar:#37474f;
  --footer:#2d3a40;
  --green:#3ccf7a;
  --white:#ffffff;
}
*{margin:0;padding:0;box-sizing:border-box}
html,body{width:678px;height:1200px;overflow:hidden;background:var(--bg)}
body{font-family:"Figtree",sans-serif;color:var(--ink)}
.board{position:relative;width:678px;height:1200px;overflow:hidden}
.abs{position:absolute}

/* section headings */
.section-title{position:absolute;right:43px;font-size:13px;color:#4a5a66;font-weight:400;letter-spacing:.2px}
.section-num{position:absolute;right:42px;font-size:50px;font-weight:300;color:transparent;-webkit-text-stroke:.8px #b9c3cc;line-height:1}

/* studio note */
.studio{position:absolute;left:30px;width:132px;text-align:center}
.studio-mark{display:flex;align-items:center;justify-content:center;gap:4px;font-size:9px;font-weight:700;color:var(--ink)}
.studio-mark span.sq{width:8px;height:8px;background:var(--ink)}
.studio p{font-size:6.2px;line-height:13.5px;color:#55636d;margin-top:20px}
.studio .regards{margin-top:12px}

/* application card */
.app-card{left:189px;top:85px;width:459px;height:339px;background:var(--white);border-radius:8px;box-shadow:0 8px 24px rgba(60,80,100,.12)}
.app-side{left:194px;top:91px;width:173px;height:327px;background:var(--blue);border-radius:4px;color:var(--white)}
.brand{font-weight:700;letter-spacing:-.2px}
.app-side .brand{position:absolute;left:14px;top:20px;font-size:8px}
.app-side h1{position:absolute;left:14px;top:89px;font-size:20.5px;line-height:21px;font-weight:800}
.app-side .lead{position:absolute;left:14px;top:148px;font-size:8.4px;font-weight:500}
.perks{position:absolute;left:14px;top:188px;width:145px;height:46px;background:var(--blue-dark);border-radius:4px;padding:11px 0 0 12px}
.perk{display:flex;align-items:center;gap:7px;font-size:5.4px;font-weight:700;height:15.5px}
.perk svg{width:9px;height:9px}
.powered{position:absolute;left:15px;top:288px;font-size:4.6px;font-weight:700}
.partners{position:absolute;left:14px;top:300px;display:flex;gap:12px;align-items:center;font-size:6.6px;font-weight:500}
.partners span.sq{display:inline-block;width:6px;height:6px;background:var(--white);margin-right:2px;vertical-align:-1px}

.form-title{left:382px;top:103px;font-size:13px;font-weight:700}
.form-sub{left:383px;top:123px;font-size:6.4px;color:var(--muted)}
.lang{left:558px;top:135px;width:78px;height:12px;background:var(--blue-soft);border-radius:3px;font-size:4.6px;color:var(--blue);text-align:center;line-height:12px;font-style:italic}
.field-label{position:absolute;font-size:5.4px;color:var(--muted)}
.input{position:absolute;height:19px;border:1px solid var(--line);border-radius:3px;background:var(--white)}
.input.filled{background:#f3fafc;border-color:var(--blue);font-size:5.6px;padding-left:6px;line-height:17px;color:var(--ink)}
.select svg{position:absolute;right:6px;top:7px;width:5px;height:4px}
.c1{left:382px;width:120px}
.c2{left:516px;width:120px}
.vehicle{left:383px;top:327px;font-size:6.4px;color:var(--blue);font-weight:500}
.cta{left:404px;top:380px;width:212px;height:23px;background:var(--blue);border-radius:3px;color:var(--white);font-size:6.4px;font-weight:600;text-align:center;line-height:23px}

/* success page */
.browser{left:153px;top:532px;width:494px;height:603px;background:var(--white);border-radius:6px;overflow:hidden;box-shadow:0 10px 30px rgba(60,80,100,.14)}
.browser-bar{position:absolute;left:0;top:0;width:100%;height:21px;background:var(--bar)}
.browser-bar i{position:absolute;top:9px;width:3.5px;height:3.5px;border-radius:50%;background:var(--white)}
.logo-pill{left:356px;top:564px;width:90px;height:21px;border-radius:11px;background:var(--blue-soft);font-size:8px;text-align:center;line-height:21px;color:var(--ink)}
.success{left:153px;width:494px;top:603px;text-align:center;font-size:22px;font-weight:800;color:var(--blue)}
.success-sub{left:153px;width:494px;top:633px;text-align:center;font-size:7px;color:#55636d}

.banner{left:188px;top:658px;width:424px;height:141px;background:var(--blue);border-radius:11px;color:var(--white)}
.banner h2{position:absolute;left:23px;top:30px;font-size:22px;font-weight:800}
.banner .amount{position:absolute;left:25px;top:59px;font-size:7.4px;font-weight:600}
.contact-pill{position:absolute;left:23px;top:82px;width:166px;height:24px;background:var(--blue-dark);border-radius:5px}
.contact-pill em{position:absolute;left:9px;top:8px;font-size:5.2px}
.next-btn{position:absolute;left:117px;top:3px;width:45px;height:18px;background:var(--yellow);border-radius:3px;color:var(--ink);font-size:5.4px;font-weight:700;text-align:center;line-height:18px}
.seal{left:454px;top:671px;width:112px;height:114px;border-radius:50%;background:radial-gradient(circle at 50% 45%,var(--yellow) 0 46%,#f2cf16 47% 56%,rgba(253,225,59,.55) 57% 70%,rgba(253,225,59,0) 72%)}
.seal-text{left:454px;top:698px;width:112px;text-align:center;color:var(--white);font-weight:700}
.seal-text .up{font-size:7px}
.seal-text .big{font-size:16px;line-height:19px;font-weight:800}
.seal-text .cap{font-size:5px;line-height:6px}

.step{position:absolute;top:817px;width:70px;height:129px;background:var(--white);border-radius:5px;box-shadow:0 3px 10px rgba(60,80,100,.08)}
.step .icon{position:absolute;left:9px;top:6px;width:30px;height:30px;border-radius:6px;background:#e6f4f8}
.step .icon svg{position:absolute;left:4px;top:4px;width:24px;height:24px}
.step h3{position:absolute;left:9px;top:47px;font-size:7px;font-weight:600;color:var(--blue)}
.step p{position:absolute;left:9px;top:63px;width:60px;font-size:5.4px;line-height:8.5px;color:var(--muted)}
.step p b{font-size:6px;letter-spacing:1.3px;color:#4a565e;font-weight:700}
.step .btn{position:absolute;left:8px;width:53px;height:14px;border-radius:3px;background:var(--blue-soft);font-size:5.4px;color:var(--blue);font-weight:600;text-align:center;line-height:14px}
.tick-badge{left:263px;top:816px;width:10px;height:10px}

.score-card{left:446px;top:812px;width:147px;height:254px;background:var(--white);border-radius:6px;box-shadow:0 3px 12px rgba(60,80,100,.08)}
.score-card .label{position:absolute;left:9px;top:7px;font-size:5.4px;color:#4a565e}
.score-pill{position:absolute;left:7px;top:17px;width:29px;height:18px;background:var(--blue-soft);border-radius:4px;font-size:10px;font-weight:700;color:var(--blue);text-align:center;line-height:18px}
.gauge{position:absolute;left:0;top:20px;width:147px;height:100px}
.score-big{position:absolute;left:0;width:147px;top:60px;text-align:center;font-size:17px;font-weight:800;color:var(--ink);line-height:18px}
.score-word{position:absolute;left:0;width:147px;top:78px;text-align:center;font-size:7px;font-style:italic;font-weight:600;color:var(--green)}
.enjoy{position:absolute;left:0;width:147px;top:117px;text-align:center;font-size:5.6px;font-weight:600;color:var(--blue)}
.perk-list{position:absolute;left:12px;top:132px;width:128px;list-style:none}
.perk-list li{position:relative;padding-left:8px;font-size:4.4px;line-height:5.8px;font-style:italic;color:var(--muted);margin-bottom:4.6px}
.perk-list li::before{content:"";position:absolute;left:0;top:2px;width:2px;height:2px;border-radius:50%;background:var(--muted)}

.limited{left:208px;top:966px;width:224px;height:100px;background:var(--yellow);border-radius:5px}
.limited p{position:absolute;left:0;width:100%;top:27px;text-align:center;font-size:7px;font-weight:500}
.act{position:absolute;left:57px;top:47px;width:106px;height:28px;border-radius:14px;background:var(--blue);color:var(--white);font-size:12px;font-weight:700;text-align:center;line-height:28px;box-shadow:0 5px 10px rgba(2,120,150,.25)}

.footer{left:153px;top:1101px;width:494px;height:34px;background:var(--footer);border-radius:0 0 6px 6px;color:var(--white)}
.footer .copy{position:absolute;left:41px;top:14px;font-size:4.8px;opacity:.85}
.footer .marks{position:absolute;right:41px;top:12px;display:flex;gap:10px;align-items:center;font-size:6.6px;font-weight:500}
.footer .marks span.sq{display:inline-block;width:6px;height:6px;background:var(--white);margin-right:2px;vertical-align:-1px}
</style>
</head>
<body>
<div class="board">

  <!-- Section 1 heading -->
  <div class="section-num" style="top:24px">01</div>
  <div class="section-title" style="top:37px">S4L Application Page</div>

  <!-- Studio note -->
  <div class="studio" style="top:146px">
    <div class="studio-mark"><span class="sq"></span>Lumenfold</div>
    <p>Tell me more about your business and any obstacle on it. We provide all of our clients with personalized web solutions providing them with 100% satisfaction.</p>
    <p class="regards">Best Regards,</p>
  </div>

  <!-- Application page -->
  <div class="abs app-card"></div>
  <div class="abs app-side">
    <div class="brand">SWIFT4LENDING</div>
    <h1>Get Your Free<br>Credit Score.</h1>
    <div class="lead">and Get Pre-Qualified Instantly</div>
    <div class="perks">
      <div class="perk"><svg viewBox="0 0 10 10"><circle cx="5" cy="5" r="5" fill="#fff"/><path d="M2.8 5.1l1.5 1.5 3-3" stroke="#02a5cb" stroke-width="1.3" fill="none"/></svg>No Social Security Number Required</div>
      <div class="perk"><svg viewBox="0 0 10 10"><circle cx="5" cy="5" r="5" fill="#fff"/><path d="M2.8 5.1l1.5 1.5 3-3" stroke="#02a5cb" stroke-width="1.3" fill="none"/></svg>No Impact On Your Credit Score</div>
    </div>
    <div class="powered">Powered by :</div>
    <div class="partners"><span><span class="sq"></span>TallyMark Rating</span><span>CrestLedger</span></div>
  </div>

  <div class="abs form-title">Get Yours Today</div>
  <div class="abs form-sub">Fill out your Information</div>
  <div class="abs lang">Para español haga clic aquí</div>

  <div class="field-label" style="left:383px;top:153px">First Name</div>
  <div class="field-label" style="left:517px;top:153px">Last Name</div>
  <div class="input filled c1" style="top:163px">Marina Costa</div>
  <div class="input c2" style="top:163px"></div>

  <div class="field-label" style="left:383px;top:187px">Address</div>
  <div class="field-label" style="left:517px;top:187px">Apartment</div>
  <div class="input c1" style="top:197px"></div>
  <div class="input c2" style="top:197px"></div>

  <div class="field-label" style="left:383px;top:222px">City</div>
  <div class="field-label" style="left:517px;top:222px">State</div>
  <div class="input c1" style="top:232px"></div>
  <div class="input c2" style="top:232px"></div>

  <div class="field-label" style="left:383px;top:256px">Zip</div>
  <div class="field-label" style="left:517px;top:256px">Date of Birth</div>
  <div class="input c1" style="top:266px"></div>
  <div class="input" style="left:516px;top:266px;width:63px"></div>
  <div class="input" style="left:583px;top:266px;width:21px"></div>
  <div class="input" style="left:608px;top:266px;width:28px"></div>

  <div class="field-label" style="left:383px;top:290px">Mobile Phone</div>
  <div class="field-label" style="left:517px;top:290px">Email</div>
  <div class="input c1" style="top:300px"></div>
  <div class="input c2" style="top:300px"></div>

  <div class="abs vehicle">The vehicle I'm most interested in is :</div>
  <div class="field-label" style="left:383px;top:339px">Category</div>
  <div class="field-label" style="left:517px;top:339px">Make</div>
  <div class="input select c1" style="top:349px"><svg viewBox="0 0 6 4"><path d="M.5.5L3 3 5.5.5" stroke="#55636d" stroke-width=".8" fill="none"/></svg></div>
  <div class="input select c2" style="top:349px"><svg viewBox="0 0 6 4"><path d="M.5.5L3 3 5.5.5" stroke="#55636d" stroke-width=".8" fill="none"/></svg></div>

  <div class="abs cta">Get Results</div>

  <!-- Section 2 heading -->
  <div class="section-num" style="top:467px">02</div>
  <div class="section-title" style="top:479px">S4L Success Page</div>

  <!-- Success page -->
  <div class="abs browser">
    <div class="browser-bar"><i style="left:459px"></i><i style="left:469px"></i><i style="left:480px"></i></div>
  </div>
  <div class="abs logo-pill brand">SWIFT4LENDING</div>
  <div class="abs success">Success!!</div>
  <div class="abs success-sub">View Your Credit Score and Pre-Qualification Amount</div>

  <div class="abs banner">
    <h2>Congratulation!</h2>
    <div class="amount">Your Pre-Qualification For Up To $75.000</div>
    <div class="contact-pill"><em>The dealer will contact you shortly, or take</em><div class="next-btn">Next Step</div></div>
  </div>
  <div class="abs seal" role="img" aria-label="Gold award seal with laurel wreath"></div>
  <div class="abs seal-text">
    <div class="up">UP TO</div>
    <div class="big">$ 75,000</div>
    <div class="cap">Pre-Qualification<br>Amount</div>
  </div>

  <!-- Steps -->
  <div class="step" style="left:207px">
    <div class="icon"><svg viewBox="0 0 24 24" fill="none" stroke="#02a5cb" stroke-width="1.2"><path d="M5 5c1-1 2-1 3 0l2 2.5c.6.8.4 1.6-.3 2.2l-1 .8c.8 1.8 2.2 3.3 4 4.2l.9-1c.6-.7 1.5-.8 2.2-.2l2.4 2c.9.8.9 1.9 0 2.8l-1 1c-5 1.4-13-6.8-12.7-12z"/><rect x="14" y="3" width="7" height="7" rx="1.2"/><circle cx="17.5" cy="5.6" r="1"/><path d="M15.7 9c.4-1 3.2-1 3.6 0"/></svg></div>
    <h3>Step 01</h3>
    <p>Call ABC Dealer at<br><b>555-014-2290</b></p>
    <div class="btn" style="top:107px">Call</div>
  </div>
  <svg class="abs tick-badge" viewBox="0 0 10 10"><circle cx="5" cy="5" r="5" fill="#02a5cb"/><path d="M2.8 5.1l1.5 1.5 3-3" stroke="#fff" stroke-width="1.2" fill="none"/></svg>

  <div class="step" style="left:283px">
    <div class="icon"><svg viewBox="0 0 24 24" fill="none" stroke="#02a5cb" stroke-width="1.2"><path d="M3 10l9-6 9 6v10H3z"/><path d="M3 10l9 6 9-6"/><rect x="7" y="4" width="10" height="8" rx="1" fill="#e6f4f8"/><path d="M12 6.5v.2M12 8v2.5"/></svg></div>
    <h3>Step 02</h3>
    <p>Email them by<br>clicking here</p>
    <div class="btn" style="top:107px">Email</div>
  </div>

  <div class="step" style="left:359px;box-shadow:none">
    <div class="icon"><svg viewBox="0 0 24 24" fill="none" stroke="#02a5cb" stroke-width="1.2"><rect x="8" y="4" width="12" height="17" rx="1.5"/><rect x="11" y="2.5" width="6" height="3" rx="1"/><path d="M12 10h5M12 13h5M12 16h5"/><circle cx="7" cy="13" r="3.5" fill="#e6f4f8"/><path d="M5.6 13l1 1 1.8-1.8"/></svg></div>
    <h3>Step 03</h3>
    <p>Print this page and<br>take it to dealer</p>
    <div class="btn" style="top:88px">Printable</div>
    <div class="btn" style="top:104px">Map to Dealer</div>
  </div>

  <!-- Score card -->
  <div class="abs score-card">
    <div class="label">Your TallyMark Rating 3.0</div>
    <div class="score-pill">760</div>
    <svg class="gauge" viewBox="0 0 147 100">
      <defs>
        <linearGradient id="arcGrad" x1="0" y1="0" x2="1" y2="0">
          <stop offset="0" stop-color="#e8306f"/>
          <stop offset=".45" stop-color="#7a4fd6"/>
          <stop offset=".75" stop-color="#3a7be0"/>
          <stop offset="1" stop-color="#2fd0b8"/>
        </linearGradient>
        <radialGradient id="dial" cx=".5" cy=".5" r=".5">
          <stop offset=".7" stop-color="#ffffff"/>
          <stop offset="1" stop-color="#eef1f4"/>
        </radialGradient>
      </defs>
      <circle cx="74" cy="51" r="38" fill="#f4f6f8"/>
      <circle cx="74" cy="51" r="29" fill="url(#dial)" stroke="#e6eaee" stroke-width="1"/>
      <path d="M31 58 A44 44 0 0 1 114 32" stroke="url(#arcGrad)" stroke-width="3" fill="none" stroke-linecap="round"/>
      <path d="M114 32 A44 44 0 0 1 118 52" stroke="#e3e8ec" stroke-width="3" fill="none"/>
      <circle cx="115" cy="37" r="3" fill="#fff" stroke="#3ccf7a" stroke-width="1.6"/>
      <path d="M108 38l2.5 8-6-4z" fill="#2f3a40"/>
      <text x="76" y="9" font-size="3.6" fill="#7a4fd6" font-family="Figtree,sans-serif">580</text>
      <text x="97" y="15" font-size="3.6" fill="#3a7be0" font-family="Figtree,sans-serif" transform="rotate(35 97 15)">640</text>
      <text x="108" y="26" font-size="3.6" fill="#2fb0c8" font-family="Figtree,sans-serif" transform="rotate(55 108 26)">700</text>
      <text x="24" y="58" font-size="3.6" fill="#e8306f" font-family="Figtree,sans-serif" transform="rotate(-90 24 58)">300</text>
      <text x="124" y="49" font-size="3.6" fill="#7a858d" font-family="Figtree,sans-serif" transform="rotate(90 124 49)">850</text>
    </svg>
    <div class="score-big">760</div>
    <div class="score-word">Excellent</div>
    <div class="enjoy">You'll soon enjoy:</div>
    <ul class="perk-list">
      <li>UNLIMITED updates to your CrestLedger Credit Report and Score</li>
      <li>Email updates of critical changes</li>
      <li>INSTANT email alerts sent as soon as CrestLedger finds out someone's applied for credit in your name</li>
      <li>Lock and Unlock your CrestLedger and Northbay Credit Credit Reports</li>
      <li>Personalized Debt Analysis &amp; Credit Score Trending</li>
      <li>Score Simulator—see how specific credit choices may affect scores</li>
      <li>UNLIMITED toll-free access to ID theft specialists</li>
      <li>Up to $1,000,000 ID Theft insurance</li>
    </ul>
  </div>

  <!-- Limited time -->
  <div class="abs limited">
    <p>Your Pre-Qualification Is Valid for a Limited Time</p>
    <div class="act">Act Now</div>
  </div>

  <!-- Footer -->
  <div class="abs footer">
    <div class="copy">© Copyright 2022 Lumenfold Studio. All Rights Reserved</div>
    <div class="marks"><span>CrestLedger</span><span class="brand">SWIFT4LENDING</span><span><span class="sq"></span>TallyMark Rating</span></div>
  </div>

</div>
</body>
</html>
```